Magazine advertisement

I need a company advertisement for magazine prints. I need to be able to scale it to different sizes if need be. I need it to showcase our brand, VornaDrive have our phone number 582.463.9047 our contact email address sales@vornadrive.net and web address www.vornadrive.net

Target Market(s)

automotive / tractor pulling

Industry/Entity Type

automotive / racing

Colors
EB3D1F
EC4F4E
F09395
F8D3D4
FCEDEE

Requirements
Must have
• our logo, our color scheme (pantone red 1795, white, black, silver

```html
<!DOCTYPE html>
<html lang="en">
<head>
<meta charset="utf-8">
<title>VornaDrive Magazine Advertisement</title>
<link href="https://fonts.googleapis.com/css2?family=Michroma&family=Exo+2:ital,wght@1,600&family=Barlow+Condensed:ital,wght@1,600&display=swap" rel="stylesheet">
<style>
  :root{
    --stage:#333333;
    --ink:#0b0b0b;
    --red:#d0211f;
    --red-deep:#8a1416;
    --white:#ffffff;
    --silver:#bfbfbf;
    --line:#3a3a3a;
  }
  *{margin:0;padding:0;box-sizing:border-box}
  html,body{width:1200px;height:1001px;overflow:hidden;background:var(--stage)}
  .ad-frame{position:absolute;left:199px;top:0;width:842px;height:1050px;transform:scale(0.9533);transform-origin:0 0}
  .ad{position:relative;width:842px;height:1050px;background:var(--ink);overflow:hidden}
  .ad-shapes{position:absolute;inset:0}
  .brand-name{position:absolute;top:128px;left:0;width:100%;text-align:center;font-family:"Michroma",sans-serif;font-size:40px;letter-spacing:1px;color:var(--red)}
  .headline{position:absolute;left:80px;top:226px;font-family:"Exo 2",sans-serif;font-style:italic;font-weight:600;font-size:60px;line-height:56px}
  .headline .red{color:var(--red)}
  .headline .white{color:var(--white)}
  .intro-panel{position:absolute;left:58px;top:417px;width:420px;height:380px;background:var(--red);border-radius:30px}
  .intro-copy{position:absolute;left:83px;top:452px;width:260px;font-family:"Barlow Condensed",sans-serif;font-style:italic;font-weight:600;font-size:25px;line-height:30px;text-transform:uppercase;color:var(--white)}
  .product-photo{position:absolute;left:352px;top:338px;width:460px;height:512px;border-radius:46% 40% 44% 48%;background:radial-gradient(circle at 40% 55%,#f2f2f2 0%,#c9c9c9 45%,#7d7d7d 80%,#3c3c3c 100%)}
  .contact-band{position:absolute;left:0;top:855px;width:842px;height:130px;background:var(--white);text-align:center}
  .contact-line{margin-top:27px;font-family:"Michroma",sans-serif;font-size:18px;color:var(--ink);display:flex;justify-content:center;align-items:center;gap:10px}
  .contact-line svg{display:block}
  .contact-item{display:flex;align-items:center;gap:5px}
  .web-address{margin-top:8px;font-family:"Michroma",sans-serif;font-size:44px;letter-spacing:2px;color:var(--ink)}
</style>
</head>
<body>
<div class="ad-frame">
  <div class="ad">
    <svg class="ad-shapes" width="842" height="1050" viewBox="0 0 842 1050">
      <defs>
        <linearGradient id="redFade" x1="0" y1="0" x2="1" y2="1">
          <stop offset="0" stop-color="#8a1416"/>
          <stop offset="0.5" stop-color="#d0211f"/>
          <stop offset="1" stop-color="#b81a1c"/>
        </linearGradient>
        <linearGradient id="redBand" x1="1" y1="0" x2="0" y2="1">
          <stop offset="0" stop-color="#e0282a"/>
          <stop offset="1" stop-color="#7a1012"/>
        </linearGradient>
      </defs>
      <polygon points="0,0 178,0 0,278" fill="url(#redFade)"/>
      <polygon points="178,0 192,0 0,296 0,278" fill="var(--white)"/>
      <polygon points="842,150 842,855 420,855" fill="url(#redBand)"/>
      <polygon points="842,130 842,150 420,855 400,855" fill="var(--white)"/>
      <line x1="842" y1="220" x2="720" y2="330" stroke="var(--white)" stroke-width="2"/>
      <line x1="842" y1="575" x2="530" y2="855" stroke="var(--white)" stroke-width="1.5"/>
      <line x1="842" y1="725" x2="640" y2="855" stroke="var(--white)" stroke-width="1.5"/>
      <line x1="842" y1="790" x2="690" y2="855" stroke="var(--white)" stroke-width="1.5"/>
      <line x1="0" y1="625" x2="60" y2="610" stroke="var(--line)" stroke-width="1.5"/>
      <line x1="0" y1="765" x2="60" y2="745" stroke="var(--line)" stroke-width="1.5"/>
      <line x1="30" y1="855" x2="110" y2="797" stroke="var(--line)" stroke-width="1.5"/>
      <line x1="150" y1="855" x2="230" y2="797" stroke="var(--line)" stroke-width="1.5"/>
      <polygon points="300,985 842,985 842,1050 260,1050" fill="url(#redBand)"/>
      <polygon points="285,985 305,985 268,1050 248,1050" fill="var(--white)"/>
      <line x1="0" y1="1050" x2="60" y2="985" stroke="var(--line)" stroke-width="1.5"/>
      <line x1="380" y1="985" x2="310" y2="1050" stroke="var(--white)" stroke-width="1.5"/>
      <line x1="600" y1="985" x2="380" y2="1050" stroke="var(--white)" stroke-width="1.5"/>
    </svg>

    <div class="brand-name">VornaDrive</div>

    <h1 class="headline">
      <span class="red">Performance.</span><br>
      <span class="white">Power.</span><br>
      <span class="red">Precision.</span>
    </h1>

    <div class="intro-panel"></div>
    <div class="product-photo" role="img" aria-label="Photo of a polished silver billet turbocharger with exposed compressor wheel"></div>
    <p class="intro-copy">We deliver high-performance solutions for those who demand quality, reliability, and real results. Our products and services are engineered to push limits, enhance efficiency, and maximize performance.</p>

    <div class="contact-band">
      <div class="contact-line">
        <span class="contact-item">
          <svg width="14" height="14" viewBox="0 0 24 24"><path d="M6.6 10.8a15 15 0 0 0 6.6 6.6l2.2-2.2c.3-.3.7-.4 1-.2 1.1.4 2.3.6 3.6.6.6 0 1 .4 1 1V20c0 .6-.4 1-1 1A17 17 0 0 1 3 4c0-.6.4-1 1-1h3.5c.6 0 1 .4 1 1 0 1.3.2 2.5.6 3.6.1.3 0 .7-.2 1z" fill="var(--red)"/></svg>
          582.463.9047
        </span>
        <span class="contact-item">
          <svg width="16" height="12" viewBox="0 0 16 12"><rect x="1" y="1" width="14" height="10" fill="none" stroke="var(--red)" stroke-width="1.5"/><polyline points="1,1 8,7 15,1" fill="none" stroke="var(--red)" stroke-width="1.5"/></svg>
          SALES@VORNADRIVE.NET
        </span>
      </div>
      <div class="web-address">VORNADRIVE.NET</div>
    </div>
  </div>
</div>
</body>
</html>
```